Marketing One-Sheet for Security Deposit Claim Notice

I need a one-sheet flyer formatted for email distribution — optimized as a JPEG/PNG that I can insert into Constant Contact or Outlook. I do not want to attach it to an email, but insert it in the email we send out. I would like it to look professional but engaging. Some images would be good, but want to make sure it reads well if images do not load for the recipients. The text is in the attached Word document, but I am open to changes/ideas that may be better for marketing purposes. I included the URLs for some of the links I would like in the one-sheet that is clickable. The logo for the business is being uploaded on the Word document. Proposed text is also uploaded in a Word document. Thank you.

Target Market(s)

Landlords, Real Estate Agents, Property Managers

Industry/Entity Type

Legal

Requirements
Must have
• Professional but appealing design. The One-sheet is going to be placed in the body of emails, not as an attachment.
Nice to have
• Include our logo for the business and the web links please.
Should not have
• Images can be ok, but it needs to look right if images do not download from the email sent out.

```html
<!DOCTYPE html>
<html lang="en">
<head>
<meta charset="utf-8">
<title>Keep the Tenant's Security Deposit</title>
<link href="https://fonts.googleapis.com/css2?family=Open+Sans:wght@400;600;700&display=swap" rel="stylesheet">
<style>
  :root {
    --red: #ff2339;
    --red-dark: #a90f1c;
    --ink: #222222;
    --grey-band: #ebebeb;
    --footer: #2b2b2b;
    --white: #ffffff;
  }
  * { box-sizing: border-box; margin: 0; padding: 0; }
  html, body { width: 1200px; height: 3024px; overflow: hidden; }
  body { position: relative; background: var(--white); font-family: "Open Sans", Arial, sans-serif; color: var(--ink); }
  .abs { position: absolute; }

  .brand { left: 0; width: 1200px; top: 22px; text-align: center; color: var(--red-dark); }
  .brand-name { font-size: 36px; font-weight: 600; letter-spacing: 1px; line-height: 1.1; }
  .brand-tag { font-size: 12px; margin-top: 4px; }
  .brand-contact { font-size: 15px; font-weight: 700; line-height: 1.35; margin-top: 4px; }

  .hero { left: 0; top: 185px; width: 1200px; height: 583px;
    background: radial-gradient(ellipse at 70% 70%, #5a5a5a 0%, #2e2e2e 45%, #151515 100%); }
  .hero-title { left: 0; width: 1200px; top: 380px; text-align: center; color: var(--white);
    font-size: 74px; font-weight: 400; line-height: 92px; letter-spacing: 0.5px; }

  .card { top: 842px; width: 343px; height: 223px; background: var(--red); border-radius: 8px; padding: 32px 30px; color: var(--white); }
  .card-num { display: inline-block; width: 36px; height: 36px; background: var(--red-dark); border-radius: 3px;
    font-size: 27px; font-weight: 700; line-height: 36px; text-align: center; margin-bottom: 8px; }
  .card-text { font-size: 30px; font-weight: 700; line-height: 39px; text-transform: uppercase; }

  .rule { left: 48px; width: 1102px; height: 3px; background: var(--red); }
  .section-head { left: 79px; font-size: 40px; font-weight: 700; line-height: 50px; letter-spacing: 0.3px; color: var(--ink); }
  .price { left: 79px; height: 60px; background: var(--red); color: var(--white); font-size: 30px; line-height: 60px; padding: 0 28px; }

  .band { left: 0; top: 1455px; width: 1200px; height: 650px; background: var(--grey-band); }
  .band-head { left: 79px; top: 1518px; font-size: 42px; font-weight: 700; letter-spacing: 0.3px; }
  .band-lead { left: 79px; top: 1602px; font-size: 27px; }
  .band-lead u { text-underline-offset: 4px; }
  .checks { left: 106px; top: 1672px; list-style: none; font-size: 27px; line-height: 53px; }
  .checks li { display: flex; align-items: center; gap: 12px; }
  .band-body { left: 79px; top: 1848px; width: 1060px; font-size: 27px; line-height: 46px; }

  .cta { left: 48px; top: 2558px; width: 1102px; height: 274px; background: var(--red); color: var(--white); }
  .cta-label { left: 33px; top: 48px; width: 219px; height: 65px; border: 3px solid var(--white);
    font-size: 40px; font-weight: 700; line-height: 58px; text-align: center; }
  .cta-text { left: 30px; top: 130px; width: 1000px; font-size: 41px; line-height: 50px; }

  .footer { left: 0; top: 2912px; width: 1200px; height: 112px; background: var(--footer); color: var(--white);
    display: flex; align-items: center; padding-left: 79px; font-size: 27px; }
  .footer-item { display: flex; align-items: center; gap: 10px; }
  .footer-sep { width: 2px; height: 30px; background: #888; margin: 0 32px; }
</style>
</head>
<body>
  <header class="abs brand">
    <div class="brand-name">Tenancy Legal Group</div>
    <div class="brand-tag">Legal Help for Landlords, Owners &amp; Property Managers</div>
    <div class="brand-contact">TenancyLegalGroup.com<br>1(877) 555-0142</div>
  </header>

  <div class="abs hero" role="img" aria-label="Photo of a judge's gavel beside an open law book on a dark desk"></div>
  <h1 class="abs hero-title">KEEP THE TENANT’S<br>SECURITY DEPOSIT</h1>

  <div class="abs card" style="left:48px"><span class="card-num">1</span><p class="card-text">Cover unpaid<br>rent</p></div>
  <div class="abs card" style="left:427px"><span class="card-num">2</span><p class="card-text">Apply to<br>legal fees and<br>costs</p></div>
  <div class="abs card" style="left:807px"><span class="card-num">3</span><p class="card-text">Charge against<br>damages to the<br>property</p></div>

  <div class="abs rule" style="top:1144px"></div>
  <h2 class="abs section-head" style="top:1192px">WE PREPARE SECURITY DEPOSIT CLAIM NOTICES</h2>
  <div class="abs price" style="top:1265px">FLAT FEE $350</div>
  <div class="abs rule" style="top:1372px"></div>

  <div class="abs band"></div>
  <h2 class="abs band-head">FOLLOW FLORIDA LAW TO KEEP THE DEPOSIT</h2>
  <p class="abs band-lead">If the Security Deposit Claim is not made <u>correctly</u> and <u>on time</u>, then:</p>
  <ul class="abs checks">
    <li><svg width="28" height="28" viewBox="0 0 28 28"><circle cx="14" cy="14" r="11.5" fill="none" stroke="#ff2339" stroke-width="2.5"/><path d="M8.5 14.5l4 4 8-9" fill="none" stroke="#ff2339" stroke-width="2.5" stroke-linecap="round" stroke-linejoin="round"/></svg>Tenant is automatically entitled to their full deposit back</li>
    <li><svg width="28" height="28" viewBox="0 0 28 28"><circle cx="14" cy="14" r="11.5" fill="none" stroke="#ff2339" stroke-width="2.5"/><path d="M8.5 14.5l4 4 8-9" fill="none" stroke="#ff2339" stroke-width="2.5" stroke-linecap="round" stroke-linejoin="round"/></svg>No claim against the deposit can be made</li>
    <li><svg width="28" height="28" viewBox="0 0 28 28"><circle cx="14" cy="14" r="11.5" fill="none" stroke="#ff2339" stroke-width="2.5"/><path d="M8.5 14.5l4 4 8-9" fill="none" stroke="#ff2339" stroke-width="2.5" stroke-linecap="round" stroke-linejoin="round"/></svg>Tenant can sue and recover the deposit and thousands in legal fees</li>
  </ul>
  <p class="abs band-body">There are lawyers that specialize in representing tenants and go after landlords that do not make a proper claim against the security deposit. They sue and win their cases and get thousands of dollars in legal fees against Landlords, even if the tenant owes unpaid rent.</p>

  <div class="abs rule" style="top:2186px"></div>
  <h2 class="abs section-head" style="top:2234px">FOR COMMERCIAL PROPERTIES, THE THE FLAT<br>LEGAL FEE IS</h2>
  <div class="abs price" style="top:2354px;padding:0 20px">$450</div>
  <div class="abs rule" style="top:2473px"></div>

  <section class="abs cta">
    <div class="abs cta-label">HIRE US</div>
    <p class="abs cta-text">to prepare and serve to the tenant the security deposit claim</p>
  </section>

  <footer class="abs footer">
    <span class="footer-item"><svg width="34" height="34" viewBox="0 0 34 34" fill="none" stroke="#fff" stroke-width="2"><circle cx="17" cy="17" r="14"/><ellipse cx="17" cy="17" rx="6" ry="14"/><path d="M3 17h28M5 10h24M5 24h24"/></svg>TenancyLegalGroup.com</span>
    <span class="footer-sep"></span>
    <span class="footer-item"><svg width="30" height="30" viewBox="0 0 24 24" fill="none" stroke="#fff" stroke-width="1.6" stroke-linejoin="round"><path d="M6.6 2.5l3 3.6-1.9 2.4a13 13 0 0 0 7.8 7.8l2.4-1.9 3.6 3-2 3.1C12 20.5 3.5 12 2.5 4.5z"/></svg>1877-555-0142</span>
  </footer>
</body>
</html>
```